PEACFUL ACUPUNCTURE PRACTITIONER NEEDS A NEW COAT

I need a new design for an exiting website http://willowgateneedlework.com/ for a acupuncturist. This will be a minimalism design with lots and lots of white space. Home page and one interior page. Please keep the feeling of calm and peaceful serenity. For Color scheme: https://www.morningfernclinic.com/fertility. The bottom part of the home page with sections and links to the service pages: https://harborlotuswellness.com/. The client likes this the best: http://mfclinic.com/. I'm attaching the logo and content pages.

Target Market(s)

Women

Industry/Entity Type

Wellness, health, wellbeing, meditation

Number of Pages Required

2 page

Font styles to use
Sans Serif
Decorative

Colors

Designer to choose colors to be used in the design.

Requirements
Must have
Nice to have
• Follow new website drafts and links
Should not have
• Busy with bright colors. No poping

```html
<!DOCTYPE html>
<html lang="en">
<head>
<meta charset="utf-8">
<title>Willowgate Acupuncture</title>
<link href="https://fonts.googleapis.com/css2?family=Crimson+Pro:ital,wght@0,400;0,500;1,400&family=Didact+Gothic&family=IM+Fell+English:ital@0;1&display=swap" rel="stylesheet">
<style>
:root{
  --rose:#c39299;
  --rose-dark:#a97f86;
  --rose-soft:#e7d7db;
  --blush:#eee2e5;
  --footer:#e9dade;
  --ink:#2c2628;
  --text:#4a4446;
  --muted:#7b7275;
  --white:#ffffff;
  --line:#e2d3d7;
}
*{box-sizing:border-box;margin:0;padding:0}
html,body{width:1200px;height:3296px;overflow:hidden;background:var(--white)}
body{position:relative;font-family:"Didact Gothic",sans-serif;color:var(--text)}
.abs{position:absolute}
.serif{font-family:"Crimson Pro",serif}

/* top bar */
.top-bar{left:0;top:0;width:1200px;height:35px;background:var(--rose-soft);display:flex;align-items:center;justify-content:center;gap:14px;font-size:13px;color:var(--ink)}
.top-bar .phone-badge{width:26px;height:26px;border-radius:50%;background:var(--rose);display:flex;align-items:center;justify-content:center}
.top-bar .phone-number{font-family:"Crimson Pro",serif;font-size:20px;color:var(--rose)}

/* nav */
.main-nav{left:0;top:35px;width:1200px;height:93px;background:var(--white)}
.main-nav a{position:absolute;top:38px;font-size:12.5px;color:var(--ink);text-decoration:none;transform:translateX(-50%);white-space:nowrap}
.main-nav a.active{color:var(--rose)}
.brand{position:absolute;left:600px;top:10px;transform:translateX(-50%);text-align:center;color:var(--rose-dark);font-family:"Crimson Pro",serif}
.brand .brand-dot{width:30px;height:30px;border-radius:50%;background:var(--rose-soft);margin:0 auto 4px}
.brand .brand-name{font-size:20px;line-height:1}
.brand .brand-sub{font-size:10px;letter-spacing:2.5px;line-height:1.3}

/* hero */
.hero{left:0;top:128px;width:1200px;height:585px;background:linear-gradient(110deg,#b9bcc4 0%,#d5d6da 35%,#c8b1a2 55%,#cfc9c6 70%,#9ea6b3 100%)}
.hero-title{left:0;top:310px;width:1200px;font-family:"IM Fell English",serif;font-weight:400;font-size:44px;line-height:54px;color:#1d1a1b;text-align:center}
.hero-sub{left:0;top:434px;width:1200px;font-family:"Crimson Pro",serif;font-style:italic;font-size:15px;line-height:21px;color:#2d2a2b;text-align:center}
.slider-arrow{width:42px;height:42px;border-radius:50%;background:rgba(255,255,255,.55);display:flex;align-items:center;justify-content:center}

/* buttons */
.btn{position:absolute;height:40px;border-radius:20px;background:var(--rose);color:var(--white);font-family:"Crimson Pro",serif;font-size:15px;letter-spacing:.5px;display:flex;align-items:center;padding:0 18px 0 46px;white-space:nowrap;border:3px solid rgba(255,255,255,.55)}
.btn::before{content:"";position:absolute;left:4px;top:3px;width:28px;height:28px;border-radius:50%;background:#f4e9eb}

/* philosophy */
.philosophy-art{left:200px;top:792px;width:335px;height:335px;border-radius:50%;background:radial-gradient(circle,#a9744a 0%,#c79a76 35%,#e7d4d8 70%,#e3d1d5 100%)}
.philosophy-title{left:609px;top:782px;font-family:"Crimson Pro",serif;font-weight:400;font-size:36px;color:var(--ink)}
.philosophy-text{left:610px;top:843px;width:370px;font-size:12.3px;line-height:20.4px;color:var(--text)}
.philosophy-text p+p{margin-top:14px}

/* services */
.services{left:0;top:1200px;width:1200px;height:697px;background:var(--blush)}
.services-title{left:0;top:1268px;width:1200px;text-align:center;font-family:"Crimson Pro",serif;font-weight:400;font-size:37px;color:var(--ink)}
.service-card{position:absolute;top:1350px;width:247px;height:337px;background:var(--white);border-radius:6px}
.service-card .service-photo{position:absolute;left:5px;top:5px;width:237px;height:172px}
.service-card h3{position:absolute;top:200px;width:100%;text-align:center;font-family:"Crimson Pro",serif;font-weight:400;font-size:21px;line-height:22px;color:var(--ink)}
.service-card .btn{left:40px;top:266px}
.services-note{left:0;top:1737px;width:1200px;text-align:center;font-size:13.5px;line-height:23px;color:var(--ink)}
.services-call{left:0;top:1796px;width:1200px;text-align:center;font-family:"Crimson Pro",serif;font-size:22px;color:var(--ink)}

/* testimonials */
.testimonials{left:0;top:1897px;width:1200px;height:472px;background:linear-gradient(180deg,#ab848b,#a27a82 60%,#9a737b)}
.testimonials-title{left:424px;top:1966px;font-family:"Crimson Pro",serif;font-weight:400;font-size:37px;color:var(--white)}
.testimonials-sub{left:428px;top:2015px;font-family:"Crimson Pro",serif;font-size:15px;color:var(--white)}
.quote-badge{left:177px;top:2101px;width:86px;height:86px;border-radius:50%;background:var(--white);display:flex;align-items:center;justify-content:center;font-family:"Crimson Pro",serif;font-size:66px;color:#c8c3c4;padding-top:26px}
.avatar{left:240px;top:2079px;width:120px;height:120px;border-radius:50%;background:#cbb6ad;border:4px solid var(--white)}
.testimonial-text{left:416px;top:2078px;width:610px;font-style:italic;font-size:13.3px;line-height:22.4px;color:var(--white)}
.testimonial-name{left:420px;top:2253px;font-family:"Crimson Pro",serif;font-size:18px;color:var(--white)}
.testimonial-name::before{content:"";display:inline-block;width:16px;height:1px;background:var(--white);vertical-align:middle;margin-right:10px}
.testimonial-role{left:446px;top:2279px;font-size:13px;color:var(--white)}

/* contact */
.contact-frame{left:137px;top:2461px;width:928px;height:345px;border:2px solid var(--line);border-top:none}
.frame-top{top:2461px;height:2px;background:var(--line)}
.frame-dot{top:2457px;width:9px;height:9px;border-radius:50%;background:var(--rose)}
.contact-title{left:0;top:2440px;width:1200px;text-align:center;font-family:"Crimson Pro",serif;font-weight:400;font-size:35px;color:var(--ink)}
.contact-intro{left:0;top:2492px;width:1200px;text-align:center;font-size:13.5px;line-height:23px;color:var(--text)}
.field{position:absolute;background:var(--white);border:1px solid #dcd3d5;border-radius:5px;font-size:11.5px;color:var(--muted);padding:14px 14px}
.field.message{padding-top:12px}

/* footer */
.site-footer{left:0;top:2902px;width:1200px;height:394px;background:var(--footer)}
.footer-brand{left:55px;top:3010px;width:275px;text-align:center;color:var(--rose-dark);font-family:"Crimson Pro",serif}
.footer-brand .brand-dot{width:60px;height:60px;border-radius:50%;background:#ddc4ca;margin:0 auto 14px}
.footer-brand .brand-name{font-size:38px;line-height:1}
.footer-brand .brand-sub{font-size:20px;letter-spacing:5px;line-height:1.4}
.footer-heading{top:2944px;font-family:"Crimson Pro",serif;font-weight:400;font-size:19px;color:var(--ink)}
.sitemap{left:337px;top:2998px;list-style:none}
.sitemap li{height:24px;font-size:12.5px;color:var(--ink);display:flex;align-items:center}
.sitemap li::before{content:"";width:5px;height:5px;border-radius:50%;background:var(--rose);margin-right:20px}
.footer-contact{left:613px;width:260px;font-size:12.5px;color:var(--ink)}
.footer-icon{left:611px}
.map-box{left:886px;top:2998px;width:253px;height:193px;background:linear-gradient(135deg,#eef0f2,#e3e6ea 60%,#dfe7e1)}
.footer-rule{left:60px;top:3251px;width:1080px;height:1px;background:#dccbd0}
.copyright{left:0;top:3266px;width:1200px;text-align:center;font-size:12px;color:var(--ink)}
</style>
</head>
<body>

<header>
  <div class="top-bar abs">
    <span>Schedule A Free 30 Minute Consultation</span>
    <span class="phone-badge">
      <svg width="14" height="14" viewBox="0 0 24 24"><path fill="#fff" d="M6.6 10.8c1.4 2.8 3.8 5.1 6.6 6.6l2.2-2.2c.3-.3.7-.4 1-.2 1.1.4 2.3.6 3.6.6.6 0 1 .4 1 1V20c0 .6-.4 1-1 1C10.6 21 3 13.4 3 4c0-.6.4-1 1-1h3.5c.6 0 1 .4 1 1 0 1.3.2 2.5.6 3.6.1.3 0 .7-.2 1L6.6 10.8z"/></svg>
    </span>
    <span class="phone-number">413-555-0186</span>
  </div>

  <nav class="main-nav abs">
    <a class="active" style="left:161px">Home</a>
    <a style="left:219px">About</a>
    <a style="left:324px">Fertility &amp; Pregnancy</a>
    <a style="left:463px">Hormone Balance</a>
    <div class="brand">
      <div class="brand-dot"></div>
      <div class="brand-name">Willowgate</div>
      <div class="brand-sub">ACUPUNCTURE</div>
    </div>
    <a style="left:743px">Strength &amp; Structure</a>
    <a style="left:882px">Emotional Wellbeing</a>
    <a style="left:997px">Online Shop</a>
    <a style="left:1087px">Testimonials</a>
  </nav>
</header>

<main>
  <section class="hero abs" role="img" aria-label="Hands resting on a pregnant belly draped in a soft grey towel"></section>
  <h1 class="hero-title abs">Specializing In Women’s Health,<br>Fertility Challenges &amp; Pregnancy Care.</h1>
  <p class="hero-sub abs">Consultations are always available to help answer any questions you may have about<br>acupuncture or herbal medicine in a relaxed environmen</p>
  <a class="btn" style="left:454px;top:497px">CONTACT US</a>
  <a class="btn" style="left:621px;top:497px">CALL US</a>
  <div class="slider-arrow abs" style="left:40px;top:386px">
    <svg width="12" height="16" viewBox="0 0 12 16"><path d="M9 1 2 8l7 7" fill="none" stroke="#7b7275" stroke-width="1.6"/></svg>
  </div>
  <div class="slider-arrow abs" style="left:1118px;top:386px">
    <svg width="12" height="16" viewBox="0 0 12 16"><path d="m3 1 7 7-7 7" fill="none" stroke="#7b7275" stroke-width="1.6"/></svg>
  </div>

  <section class="philosophy">
    <div class="philosophy-art abs" role="img" aria-label="Acupuncture treatment photo framed in a lotus-shaped border"></div>
    <h2 class="philosophy-title abs">Philosophy Of Care</h2>
    <div class="philosophy-text abs">
      <p>Acupuncture &amp; Chineses Herbal Medicine are rooted In Over 3000 years of History and tradition. As a complete medical system that has remained flexible and relevent We Honor What Has Worked from the Past While embracing the Medicine of tomorrow.</p>
      <p>At Willowgate Acupuncture We provide compassionate, respectful and empowering care in a safe and Inclusive Environment. Our goal is to harmonize physical, Mental and emotional wellbeing to strengthen the calm center from which we all strive to live.</p>
    </div>
    <a class="btn" style="left:608px;top:1084px">LEARN MORE</a>
  </section>

  <section class="services abs"></section>
  <h2 class="services-title abs">Services We Provide</h2>
  <article class="service-card" style="left:72px">
    <div class="service-photo" role="img" aria-label="White eggs resting in a straw nest" style="background:linear-gradient(160deg,#8a6a45,#d9d2c0 50%,#6e5334)"></div>
    <h3>Fertility &amp;<br>Pregnancy</h3>
    <a class="btn">LEARN MORE</a>
  </article>
  <article class="service-card" style="left:342px">
    <div class="service-photo" role="img" aria-label="Calm lake with dark stones at sunset" style="background:linear-gradient(180deg,#d9a36a,#5f6a80 35%,#2d3544 80%,#1d222c)"></div>
    <h3>Hormone<br>Balance</h3>
    <a class="btn">LEARN MORE</a>
  </article>
  <article class="service-card" style="left:612px">
    <div class="service-photo" role="img" aria-label="Large old tree with spreading roots in a green forest" style="background:linear-gradient(160deg,#c9d07a,#6f8a3a 45%,#7a6a48 80%)"></div>
    <h3>Strength &amp;<br>Structure</h3>
    <a class="btn">LEARN MORE</a>
  </article>
  <article class="service-card" style="left:882px">
    <div class="service-photo" role="img" aria-label="Pregnant belly with a painted heart, soft white clothing" style="background:linear-gradient(160deg,#f1eeee,#e8dcd8 50%,#d9c3bd)"></div>
    <h3>Emotional<br>Wellbeing</h3>
    <a class="btn">LEARN MORE</a>
  </article>
  <p class="services-note abs">Consultations are always available to help answer any questions you may have about<br>acupuncture or herbal medicine in a relaxed environment.</p>
  <p class="services-call abs">Call Us On : 413-555-0186</p>

  <section class="testimonials abs" role="img" aria-label="Woman walking in shallow sea water, tinted rose"></section>
  <h2 class="testimonials-title abs">Testimonials</h2>
  <p class="testimonials-sub abs">What Our Patients Are Saying About Us...</p>
  <div class="quote-badge abs">“</div>
  <div class="avatar abs" role="img" aria-label="Portrait of the reviewer"></div>
  <p class="testimonial-text abs">I bring over 35 years of experience to my massage/bodywork practice and am fascinated by the new insights and techniques I am learning. My experience includes extensive knowledge in swedish massage, Deep Tissue, Cranial Sacral Therapy, Shiatsu, supported stretching, and visceral manipulation. Also a dancer and yogi, I incorporate this intelligence into my bodywork. Integrative Bodywork facilitates structural and neuromuscular repatterning, relaxation, and overall healing.&nbsp;&nbsp;I have effectively worked with a variety of conditions, in conjunction with a client's medical professional...... <u>Read More</u></p>
  <p class="testimonial-name abs">Daniel R.</p>
  <p class="testimonial-role abs">Business Owner</p>
  <svg class="abs" style="left:74px;top:2128px" width="20" height="36" viewBox="0 0 20 36"><path d="M18 2 2 18l16 16" fill="none" stroke="#fff" stroke-width="1.8"/></svg>
  <svg class="abs" style="left:1106px;top:2128px" width="20" height="36" viewBox="0 0 20 36"><path d="m2 2 16 16L2 34" fill="none" stroke="#fff" stroke-width="1.8"/></svg>

  <section class="contact">
    <div class="contact-frame abs"></div>
    <div class="frame-top abs" style="left:137px;width:330px"></div>
    <div class="frame-top abs" style="left:736px;width:329px"></div>
    <div class="frame-dot abs" style="left:464px"></div>
    <div class="frame-dot abs" style="left:727px"></div>
    <h2 class="contact-title abs">Contact Us</h2>
    <p class="contact-intro abs">An acupuncturist specializing in women’s health, fertility challenges and<br>pregnancy care in Easthollow MA.</p>
    <div class="field" style="left:225px;top:2573px;width:240px;height:41px">Name *</div>
    <div class="field" style="left:480px;top:2573px;width:239px;height:41px">Email *</div>
    <div class="field" style="left:735px;top:2573px;width:239px;height:41px">Subject *</div>
    <div class="field message" style="left:225px;top:2629px;width:749px;height:112px">Message *</div>
    <a class="btn" style="left:536px;top:2785px">SUBMIT</a>
  </section>
</main>

<footer class="site-footer abs"></footer>
<div class="footer-brand abs">
  <div class="brand-dot"></div>
  <div class="brand-name">Willowgate</div>
  <div class="brand-sub">ACUPUNCTURE</div>
</div>

<h3 class="footer-heading abs" style="left:337px">Sitemap</h3>
<ul class="sitemap abs">
  <li>Home</li><li>About</li><li>Fertility &amp; Pregnancy</li><li>Hormone Balance</li><li>Strength &amp; Structure</li><li>Emotional Wellbeing</li><li>Online Shop</li><li>Testimonials</li><li>Contact Us</li>
</ul>

<h3 class="footer-heading abs" style="left:613px">Contact Us</h3>
<svg class="footer-icon abs" style="top:3012px" width="18" height="26" viewBox="0 0 18 26"><path d="M9 1C4.6 1 1 4.5 1 8.9 1 15 9 25 9 25s8-10 8-16.1C17 4.5 13.4 1 9 1z" fill="none" stroke="#c39299" stroke-width="1.8"/><circle cx="9" cy="9" r="3" fill="none" stroke="#c39299" stroke-width="1.8"/></svg>
<p class="footer-contact abs" style="left:648px;top:2996px;line-height:20px">Willowgate Acupuncture<br><span style="display:block;margin-top:5px">48 Alder Row<br>Easthollow, MA 01099</span></p>
<svg class="footer-icon abs" style="top:3075px" width="22" height="22" viewBox="0 0 24 24"><path fill="none" stroke="#c39299" stroke-width="1.6" d="M6.6 10.8c1.4 2.8 3.8 5.1 6.6 6.6l2.2-2.2c.3-.3.7-.4 1-.2 1.1.4 2.3.6 3.6.6.6 0 1 .4 1 1V20c0 .6-.4 1-1 1C10.6 21 3 13.4 3 4c0-.6.4-1 1-1h3.5c.6 0 1 .4 1 1 0 1.3.2 2.5.6 3.6.1.3 0 .7-.2 1L6.6 10.8z"/></svg>
<p class="footer-contact abs serif" style="left:648px;top:3073px;font-size:18px">413-555-0186</p>
<svg class="footer-icon abs" style="top:3116px" width="22" height="22" viewBox="0 0 22 22"><circle cx="11" cy="11" r="9.5" fill="none" stroke="#c39299" stroke-width="1.6"/><path d="M11 5v6l4 2" fill="none" stroke="#c39299" stroke-width="1.6"/></svg>
<p class="footer-contact abs" style="left:648px;top:3116px;line-height:22px">Working Hours:<br><span style="display:block;margin-top:4px;font-size:13.5px" class="serif">Tuesday – Friday 10-6<br>Saturday 10-3</span></p>

<h3 class="footer-heading abs" style="left:888px">Location Map</h3>
<div class="map-box abs" role="img" aria-label="Street map showing the clinic location"></div>
<div class="footer-rule abs"></div>
<p class="copyright abs">©2021 Willowgate Acupuncture - All rights reserved.</p>

</body>
</html>
```